Stationary and Business card design for a residential window and door manufacturing company
residential window and door manufacturing company
Simple
Tom Ashdale
General Manager
3870 Pellham Ridge Rd Toronto, ON M8K 2T6
t.ashdale@solvarowindowsanddoors.com
solvarowindowsanddoors.com
Side ways logo

```html
<!DOCTYPE html>
<html lang="en">
<head>
<meta charset="utf-8">
<title>Solvaro Windows &amp; Doors — Business Card</title>
<link href="https://fonts.googleapis.com/css2?family=Open+Sans:wght@400;600;700;800&display=swap" rel="stylesheet">
<style>
  :root {
    --backdrop: #7d7f80;
    --card-white: #ffffff;
    --card-black: #0b0b0b;
    --brand-red: #e3262b;
    --ink-dark: #2b2b2b;
    --ink-mid: #5a5a5a;
    --silver: #bdbdbd;
  }
  * { box-sizing: border-box; margin: 0; padding: 0; }
  html, body {
    width: 1200px; height: 904px; overflow: hidden;
    background: var(--backdrop);
    font-family: "Open Sans", Arial, sans-serif;
  }
  .stage {
    width: 1200px; height: 904px;
    display: flex; align-items: center; justify-content: center; gap: 80px;
  }
  .card {
    width: 360px; height: 600px;
    position: relative;
    box-shadow: 0 14px 30px rgba(0,0,0,0.35);
    overflow: hidden;
  }
  .card-back {
    background: var(--card-black);
    display: flex; align-items: center; justify-content: center;
  }
  .back-wordmark {
    display: flex; align-items: center; gap: 12px;
    color: var(--silver);
    font-weight: 800; font-size: 34px; letter-spacing: 3px;
    text-transform: uppercase;
  }
  .back-wordmark .mark-square {
    width: 22px; height: 22px; background: var(--silver);
  }
  .card-front {
    background: var(--card-white);
    display: flex; flex-direction: column; align-items: center;
  }
  .front-wordmark {
    margin-top: 120px;
    display: flex; align-items: center; gap: 12px;
    color: var(--ink-dark);
    font-weight: 800; font-size: 36px; letter-spacing: 3px;
    text-transform: uppercase;
  }
  .front-wordmark .mark-square {
    width: 22px; height: 22px; background: var(--brand-red);
  }
  .holder { margin-top: 90px; text-align: center; }
  .holder-name {
    color: var(--brand-red); font-weight: 700; font-size: 22px;
  }
  .holder-title {
    color: var(--ink-mid); font-size: 14px; margin-top: 2px;
  }
  .contact {
    margin-top: 56px; width: 100%; padding: 0 40px;
    color: var(--ink-dark); font-size: 12.5px; line-height: 1.75;
    text-align: center;
  }
  .phones { display: flex; justify-content: center; gap: 22px; }
  .phone { display: inline-flex; align-items: center; gap: 5px; }
  .phone svg { width: 12px; height: 12px; fill: var(--brand-red); }
  .front-band {
    position: absolute; left: 0; right: 0; bottom: 0; height: 22px;
    background: var(--brand-red);
  }
</style>
</head>
<body>
  <main class="stage">
    <section class="card card-back" aria-label="Card back">
      <div class="back-wordmark"><span class="mark-square"></span>Solvaro</div>
    </section>

    <section class="card card-front" aria-label="Card front">
      <div class="front-wordmark"><span class="mark-square"></span>Solvaro</div>

      <div class="holder">
        <p class="holder-name">Tom Ashdale</p>
        <p class="holder-title">General Manager</p>
      </div>

      <div class="contact">
        <div class="phones">
          <span class="phone">
            <svg viewBox="0 0 24 24" aria-hidden="true"><path d="M6.6 10.8a15.1 15.1 0 0 0 6.6 6.6l2.2-2.2a1 1 0 0 1 1-.25 11.4 11.4 0 0 0 3.6.57 1 1 0 0 1 1 1V20a1 1 0 0 1-1 1A17 17 0 0 1 3 4a1 1 0 0 1 1-1h3.5a1 1 0 0 1 1 1c0 1.25.2 2.45.57 3.6a1 1 0 0 1-.25 1z"/></svg>
            905.555.0187
          </span>
          <span class="phone">
            <svg viewBox="0 0 24 24" aria-hidden="true"><path d="M7 2h10a2 2 0 0 1 2 2v16a2 2 0 0 1-2 2H7a2 2 0 0 1-2-2V4a2 2 0 0 1 2-2zm0 3v13h10V5zm5 14.2a1 1 0 1 0 0 .01z"/></svg>
            416.555.0142
          </span>
        </div>
        <p>t.ashdale@solvarowindowsanddoors.com</p>
        <p>3870 Pellham Ridge Rd Toronto, ON M8K 2T6</p>
        <p>solvarowindowsanddoors.com</p>
      </div>

      <div class="front-band"></div>
    </section>
  </main>
</body>
</html>
```